" MAIOR PARTE DO ATENDIMENTO SERÁ ONLINE, PODENDO OPTAR POR VISITAR AS FAZENDAS OU NÃO. DEVIDO O ATENDIMENTO AOS CLIENTES SER DE FORMA DIGITAL, MARCAMOS REUNIÃO ATRAVÉS DE VÍDEO CONFERÊNCIA, ASSIM TIRANDO SUAS DÚVIDAS E EXPLICANDO OS SERVIÇOS FORNECIDOS... TODAS AS INFORMAÇÕES OBTIDAS EM CONVERSA COM O CLIENTE SÃO UNIFICADAS COM AS INFORMAÇÕES QUE OBTEMOS ATRAVÉS DE IMAGENS DE SATÉLITE, E ATRAVÉS DE UMA RELATÓRIO CONSEGUIMOS EXPLICAR COMO ESTÁ A SUA FAZENDA, QUAL É O MELHOR MÉTODO DE MANEJO PARA A SAFRA, SE HÁ OU NÃO ÁREAS DEGRADADAS, EXPLICAMOS PARA ELE, QUAIS AS QUANTIDADE E QUAIS OS LOCAIS DEVERÃO RECEBER APLICAÇÃO DE ADUBO. A AGRICULTURA DE PRECISÃO NÃO É UM APARELHO ELA É UMA TÉCNICA PARA OTIMIZARMOS OS CUSTOS. DEIXAMOS DE TRATAR UMA PROPRIEDADE DE FORMA GERAL, E TRATAMOS CADA TALHÃO OU CADA PASTO DE FORMA DIFERENTE, DE ACORDO COM SUA NECESSIDADE, ASSIM DIMINUINDO CUSTOS E MELHORANDO A PRODUÇÃO DA PROPRIEDADE, E CONSEQUENTEMENTE, MELHORANDO O RETORNO FINANCEIRO DO PRODUTOR RURAL. "

```html
<!DOCTYPE html>
<html lang="pt-BR">
<head>
<meta charset="utf-8">
<title>Papel timbrado – Terravia</title>
<link href="https://fonts.googleapis.com/css2?family=Arimo:wght@400;700&display=swap" rel="stylesheet">
<style>
  :root {
    --backdrop: #e4e4e4;
    --paper: #ffffff;
    --ink: #1a1a1a;
    --ink-soft: #555555;
    --gold: #b8924a;
    --gold-light: #e6cd8c;
    --gold-dark: #8a6a2e;
  }
  * { box-sizing: border-box; margin: 0; padding: 0; }
  html, body {
    width: 1200px; height: 1200px; overflow: hidden;
    background: var(--backdrop);
    font-family: "Arimo", Arial, sans-serif;
  }
  .letterhead {
    position: absolute; left: 197px; top: 30px;
    width: 806px; height: 1140px;
    background: var(--paper);
    overflow: hidden;
  }
  .brand {
    position: absolute; left: 36px; top: 48px;
    display: flex; align-items: center; gap: 12px;
  }
  .brand-square {
    width: 30px; height: 30px; background: var(--gold);
  }
  .brand-text { display: flex; flex-direction: column; }
  .brand-name {
    font-size: 34px; font-weight: 400; letter-spacing: 8px;
    color: var(--ink-soft); line-height: 1;
  }
  .brand-tagline {
    margin-top: 4px;
    font-size: 9px; letter-spacing: 1.6px; color: var(--gold);
  }
  .letter-body {
    position: absolute; left: 36px; top: 275px; width: 676px;
    color: var(--ink); font-size: 16.5px; line-height: 1.2;
  }
  .letter-body p + p { margin-top: 18px; }
  .contact-list {
    position: absolute; left: 36px; top: 855px;
    list-style: none; font-size: 10px; color: var(--ink-soft);
  }
  .contact-list li {
    display: flex; align-items: flex-start; gap: 8px; margin-bottom: 9px;
    line-height: 1.25;
  }
  .contact-list svg { width: 10px; height: 10px; flex: none; margin-top: 1px; }
  .gold-band {
    position: absolute; left: 0; bottom: 0; width: 100%; height: 14px;
    background: linear-gradient(90deg, var(--gold-dark), var(--gold-light) 45%, var(--gold) 75%, var(--gold-light));
  }
</style>
</head>
<body>
  <main class="letterhead">
    <header class="brand">
      <div class="brand-square"></div>
      <div class="brand-text">
        <span class="brand-name">TERRAVIA</span>
        <span class="brand-tagline">AGRICULTURA DE PRECISÃO</span>
      </div>
    </header>

    <section class="letter-body">
      <p>Lorem ipsum dolor sit amet, ne vis ipsum detraxit forensibus. Vim ad dicta disputando, facete expetendis sea ne. At omnium vidisse referrentur cum. Id vel quas dicunt platonem, vim at veniam commodo adversarium, per an fabulas reformidans. Ad delenit appareat vel, denique minimum intellegam et has.</p>
      <p>Nec ex albucius moderatius. Essent salutandi pri id, no has porro commune. Iusto dolore definitionem mea et, eleifend salutatus at vel. Ignota apeirian duo an, nam no liber cetero, sit legere saperet quaestio te. Sit ei oratio invenire platonem, nam ex congue primis conclusionemque, eos case albucius voluptatum cu.</p>
      <p>Sea ea summo senserit, ne pri accusam electram corrumpit. Hinc forensibus cu est, sed id invenire persequeris. Accumsan lucilius reformidans et sea. Duo laudem dolorem ne.</p>
      <p>Illud minimum duo ut. Docendi abhorreant quo no, duo ad appetere eleifend persequeris, blandit assentior disputationi no mea. Pro id movet cetero aeterno, in prima nusquam deseruisse pri, errem petentium et vis. Mollis aliquip admodum nec te, eu falli nullam utroque nec, vitae invenire iudicabit eu eam.</p>
      <p>Mei viderer adipisci corrumpit te, dissentias intellegebat per eu. An solum decore luptatum mei, in brute scripta disputationi vel. Semper gubergren quo no. In quo regione placerat, quod legere nam ad.</p>
    </section>

    <ul class="contact-list">
      <li>
        <svg viewBox="0 0 10 10" aria-hidden="true"><path fill="#b8924a" d="M2 0.5 3.6 2.6 2.7 3.7c.6 1.4 1.9 2.8 3.5 3.5l1.1-.9L9.5 8l-1 1.5C4.6 9.3.7 5.4.5 1.5z"/></svg>
        <span>(00) 91234.5678 / 93456.7890</span>
      </li>
      <li>
        <svg viewBox="0 0 10 10" aria-hidden="true"><rect x="0.5" y="1.5" width="9" height="7" fill="none" stroke="#b8924a"/><path d="M0.5 1.5 5 5.5 9.5 1.5" fill="none" stroke="#b8924a"/></svg>
        <span>contato@terravia.com.br</span>
      </li>
      <li>
        <svg viewBox="0 0 10 10" aria-hidden="true"><circle cx="5" cy="5" r="4.3" fill="none" stroke="#b8924a"/><ellipse cx="5" cy="5" rx="1.8" ry="4.3" fill="none" stroke="#b8924a"/><path d="M0.7 5h8.6" stroke="#b8924a"/></svg>
        <span>www.terravia.com.br</span>
      </li>
      <li>
        <svg viewBox="0 0 10 10" aria-hidden="true"><path fill="#b8924a" d="M5 0.3a3.3 3.3 0 0 0-3.3 3.3C1.7 6 5 9.7 5 9.7s3.3-3.7 3.3-6.1A3.3 3.3 0 0 0 5 .3zm0 4.6a1.3 1.3 0 1 1 0-2.6 1.3 1.3 0 0 1 0 2.6z"/></svg>
        <span>Rua das Lavouras, 120, Centro<br>CEP 14800.000 - Campo Verde-SP</span>
      </li>
    </ul>

    <div class="gold-band"></div>
  </main>
</body>
</html>
```